Compass of Quiet Mornings book cover design

Book cover - the book contains 52 chapters - 2 for each letter of the alphabet, so a yearlong focus on Leadership. The Intent is to communicate that leadership is common sense. It just isn’t common practice. This book allows the reader to focus on one leadership word each week for a yearlong focus on improving one’s leadership. It is full of stories relating to the 52 words that will challenge and inspire the reader.
Target Market(s)
Leaders / Emerging Leaders
Industry/Entity Type
All
Requirements
Must have
- Appeal to executives
Nice to have
- Simplicity
Should not have
- Cartoon feel

```html
<!DOCTYPE html>
<html lang="en">
<head>
<meta charset="utf-8">
<title>Compass of Quiet Mornings – Book Cover</title>
<link rel="stylesheet" href="https://fonts.googleapis.com/css2?family=Bebas+Neue&family=Oswald:wght@600&family=Poppins:wght@600&display=swap">
<style>
  :root {
    --page-bg: #ffffff;
    --cover-black: #05080d;
    --ink-dark: #0b0b0b;
    --white: #ffffff;
    --warm-red: #e2401c;
    --warm-orange: #f39a1e;
    --warm-yellow: #f7dc45;
    --haze: #f4f4e6;
    --teal: #2fa79a;
    --teal-deep: #0f6e6e;
    --gold-edge: #e8bf52;
    --gold-light: #faf976;
  }
  * { margin: 0; padding: 0; box-sizing: border-box; }
  html, body {
    width: 1200px;
    height: 1200px;
    overflow: hidden;
    background: var(--page-bg);
  }
  .book-cover {
    position: absolute;
    left: 241px;
    top: 65px;
    width: 718px;
    height: 1077px;
    background: var(--cover-black);
    overflow: hidden;
    box-shadow: -10px 14px 22px rgba(0, 0, 0, 0.28);
  }
  .cover-art {
    position: absolute;
    left: 0;
    top: 0;
    width: 100%;
    height: 500px;
    background:
      linear-gradient(to bottom, rgba(5, 8, 13, 0) 0%, rgba(5, 8, 13, 0) 62%, rgba(5, 8, 13, 0.55) 82%, var(--cover-black) 100%),
      linear-gradient(100deg, var(--warm-red) 0%, var(--warm-orange) 18%, var(--warm-yellow) 38%, var(--haze) 58%, #bfe5da 72%, var(--teal) 88%, var(--teal-deep) 100%);
  }
  .author-name {
    position: absolute;
    top: 26px;
    left: 0;
    width: 100%;
    text-align: center;
    font-family: "Oswald", sans-serif;
    font-weight: 600;
    font-size: 44px;
    line-height: 1;
    letter-spacing: 0.42em;
    padding-left: 0.42em;
    color: var(--ink-dark);
  }
  .cover-title {
    position: absolute;
    left: 0;
    top: 0;
    width: 718px;
    height: 1077px;
  }
  .title-main {
    font-family: "Bebas Neue", sans-serif;
    fill: url(#gold-fill);
  }
  .title-link {
    font-family: "Bebas Neue", sans-serif;
    fill: var(--white);
  }
  .title-rule { fill: var(--white); }
  .cover-blurb {
    position: absolute;
    left: 50px;
    top: 936px;
    width: 618px;
    text-align: center;
    font-family: "Poppins", sans-serif;
    font-weight: 600;
    font-size: 21px;
    line-height: 35px;
    color: var(--white);
  }
</style>
</head>
<body>
  <div class="book-cover">
    <div class="cover-art" role="img" aria-label="Silhouettes of business people in suits standing in a row with a leader on stepped blocks, over an orange-yellow-teal faceted background reflecting on a glossy floor"></div>

    <p class="author-name">AUTHOR NAME</p>

    <svg class="cover-title" viewBox="0 0 718 1077" aria-label="Compass of Quiet Mornings">
      <defs>
        <linearGradient id="gold-fill" x1="0" y1="0" x2="1" y2="0">
          <stop offset="0" stop-color="var(--gold-edge)"/>
          <stop offset="0.5" stop-color="var(--gold-light)"/>
          <stop offset="1" stop-color="var(--gold-edge)"/>
        </linearGradient>
      </defs>
      <text class="title-main" x="53" y="635" font-size="173" textLength="611" lengthAdjust="spacingAndGlyphs">COMPASS</text>
      <rect class="title-rule" x="53" y="670" width="180" height="8"/>
      <text class="title-link" x="359" y="704" font-size="76" text-anchor="middle">OF QUIET</text>
      <rect class="title-rule" x="485" y="670" width="179" height="8"/>
      <text class="title-main" x="53" y="921" font-size="287" textLength="611" lengthAdjust="spacingAndGlyphs">MORNINGS</text>
    </svg>

    <p class="cover-blurb">Lorem ipsum dolor sit amet, consectetur adipisicing elit, sed do eiusmod tempor incididunt ut labore et dolore magna aliqua.</p>
  </div>
</body>
</html>
```